Designing a front label called Ice Secco / Bottle Label for a Sparkling Wine called Vello Frost

We want to bring a Vello Frost on the market. For this we need a front label. Bottle is painted white and the capsule is fixed. (Black with golden lettering K.Wendlicher) Height of label max. 8.5cm. The whole thing should be fresh teen. Happy with reference to Ice .... etc. Secco is the German version of Prosecco. But better. There are currently many Vello Frost on the market. We also want one now. www.wendlicher.de We have a nice white lacquered TRV bottle with capsule. it just fehtl the right label. Sender K.Wendlicher does not have to be on top ... but if it fits. Lettering is already in the capsule anyway.

Target Market(s)

Supermarket, gals, party, alcohol, RRP 4.99 €

Font styles to use
Decorative

Colors

Requirements
Must have
• Self-adhesive label, printable data in 4c, reference to ice, black, golden reference to the capsule.
Nice to have
• Ice cubes, cool, cool.
Should not have
• boredom

```html
<!DOCTYPE html>
<html lang="en">
<head>
<meta charset="utf-8">
<title>Vello Frost – Front Label</title>
<link rel="stylesheet" href="https://fonts.googleapis.com/css2?family=Great+Vibes&display=swap">
<style>
  :root {
    --canvas-bg: #ecebe7;
    --label-black: #000000;
    --gold: #d8b46a;
    --ice-tone-top: #dbe9e2;
    --ice-tone-bottom: #c5d6ce;
  }
  html, body {
    margin: 0;
    padding: 0;
    width: 1200px;
    height: 1200px;
    overflow: hidden;
    background: var(--canvas-bg);
  }
  .canvas {
    position: relative;
    width: 1200px;
    height: 1200px;
  }
  .front-label {
    position: absolute;
    left: 50px;
    top: 50px;
    width: 1100px;
    height: 1100px;
    background: var(--label-black);
    border-radius: 40px;
    overflow: hidden;
  }
  .brand-wordmark {
    position: absolute;
    left: 110px;
    top: 330px;
    margin: 0;
    font-family: "Great Vibes", cursive;
    font-weight: 400;
    font-size: 190px;
    line-height: 1;
    color: var(--gold);
    transform: rotate(-14deg);
    transform-origin: left bottom;
    white-space: nowrap;
  }
  .gold-band-line {
    position: absolute;
    left: 0;
    width: 100%;
    height: 3px;
    background: var(--gold);
  }
  .gold-band-line.top { top: 904px; }
  .gold-band-line.bottom { top: 1007px; }
  .ice-cube {
    position: absolute;
    left: 386px;
    top: 744px;
    width: 365px;
    height: 356px;
    border-radius: 30px 30px 14px 14px;
    background: linear-gradient(180deg, var(--ice-tone-top), var(--ice-tone-bottom));
  }
</style>
</head>
<body>
  <main class="canvas">
    <section class="front-label">
      <h1 class="brand-wordmark">Vello Frost</h1>
      <div class="gold-band-line top"></div>
      <div class="gold-band-line bottom"></div>
      <div class="ice-cube" role="img" aria-label="Photo of an ice cube set on the gold band"></div>
    </section>
  </main>
</body>
</html>
```